Kesrow Consulting- executive coaching business

looking for business card design for a newly started coaching business.
specialising in Exective coaching, Leadership, NLP and Motivation.
Looking for a simple, classy design using the existing logo attached and colour themes that complement the logo.
No red or orange in the business card design please.

Target Market(s)

Defence and Veteran community

Industry/Entity Type

Life Coaching

Contact Information for Business Card

looking for business cards for newly started coaching business.
specialising in Exective Coaching, Leadership, NLP and Motivation

Font styles to use
Serif
Script

Colors
0556a4
3176b5
86cfc6
33b8a4

Requirements
Must have
• Logo
• Email address- Lena@kesrowconsulting.com.au
• Contact number
• Services provided - Executive Coaching, Leadership, NLP and Motivational Mapping.
Nice to have
• Same colours as logo
Should not have
• Red or orange

```html
<!DOCTYPE html>
<html lang="en">
<head>
<meta charset="utf-8">
<title>Kesrow Consulting – Business Card</title>
<link rel="stylesheet" href="https://fonts.googleapis.com/css2?family=Open+Sans:wght@400;600;700&display=swap">
<style>
  :root {
    --brand-blue: #1273bd;
    --brand-grey: #8c8c8c;
    --paper: #ffffff;
    --backdrop: #e9ebee;
    --ink-light: #ffffff;
  }
  * { box-sizing: border-box; margin: 0; padding: 0; }
  html, body {
    width: 1200px; height: 900px; overflow: hidden;
    background: var(--backdrop);
    font-family: "Open Sans", Arial, sans-serif;
  }
  .canvas { position: relative; width: 1200px; height: 900px; }

  .card {
    position: absolute;
    background: var(--paper);
    box-shadow: 0 6px 18px rgba(0,0,0,0.12);
    overflow: hidden;
  }

  /* Front */
  .card--front { left: 78px; top: 34px; width: 588px; height: 364px; }
  .brand {
    position: absolute; left: 32px; top: 48px;
    display: flex; align-items: center; gap: 20px;
  }
  .brand__mark {
    width: 92px; height: 92px; border-radius: 50%;
    border: 3px solid var(--brand-grey);
  }
  .brand__name {
    font-size: 29px; font-weight: 600; letter-spacing: 0.3px;
    color: var(--brand-blue); text-transform: uppercase;
  }
  .front-band {
    position: absolute; left: 0; top: 175px; width: 100%; height: 189px;
    background: var(--brand-blue); color: var(--ink-light);
    padding: 41px 30px 0;
  }
  .person__name { font-size: 21px; font-weight: 700; line-height: 1.2; }
  .person__role { font-size: 15px; line-height: 1.3; }
  .contact { list-style: none; margin-top: 33px; }
  .contact__item {
    display: flex; align-items: center; gap: 8px;
    font-size: 15.5px; line-height: 24px;
  }
  .contact__icon { width: 12px; height: 12px; flex: none; }

  /* Back */
  .card--back { left: 388px; top: 505px; width: 566px; height: 352px; }
  .services {
    position: absolute; left: 0; top: 110px; width: 100%; height: 131px;
    background: var(--brand-blue); color: var(--ink-light);
    text-align: center; padding-top: 25px;
  }
  .services__title { font-size: 21px; font-weight: 600; line-height: 1.3; }
  .services__list { font-size: 15px; font-weight: 600; line-height: 21px; margin-top: 8px; }
</style>
</head>
<body>
<main class="canvas">

  <section class="card card--front" aria-label="Business card front">
    <header class="brand">
      <span class="brand__mark" aria-hidden="true"></span>
      <span class="brand__name">Kesrow Consulting</span>
    </header>
    <div class="front-band">
      <p class="person__name">Daniel Harper</p>
      <p class="person__role">Managing Director</p>
      <ul class="contact">
        <li class="contact__item">
          <svg class="contact__icon" viewBox="0 0 24 24" aria-hidden="true"><path fill="#ffffff" d="M6.6 10.8a15.1 15.1 0 0 0 6.6 6.6l2.2-2.2a1 1 0 0 1 1-.25 11.4 11.4 0 0 0 3.6.57 1 1 0 0 1 1 1V20a1 1 0 0 1-1 1A17 17 0 0 1 3 4a1 1 0 0 1 1-1h3.5a1 1 0 0 1 1 1c0 1.25.2 2.46.57 3.6a1 1 0 0 1-.25 1z"/></svg>
          (044)-555-0192
        </li>
        <li class="contact__item">
          <svg class="contact__icon" viewBox="0 0 24 24" aria-hidden="true"><rect x="1" y="4" width="22" height="16" fill="#ffffff"/><path d="M1.5 4.5l10.5 8.5 10.5-8.5" fill="none" stroke="#1273bd" stroke-width="2"/></svg>
          info@yourmail.example
        </li>
      </ul>
    </div>
  </section>

  <section class="card card--back" aria-label="Business card back">
    <div class="services">
      <h2 class="services__title">Services provided</h2>
      <p class="services__list">Executive Coaching&nbsp; | &nbsp;Leadership&nbsp; | &nbsp;NLP<br>Motivational Mapping</p>
    </div>
  </section>

</main>
</body>
</html>
```